Corporate Web Design

Hello Designers,
Thank you for wanting to participate in designing a web design.
First off let me introduce ourselves, we are a precious metals refinery that is base in the west coast. Our Name is Harborline Precious Metals Refinery. Our sole goal for this website is simplicity yet cleanliness and elegance. We want to demonstrate the process and procedures of what we do and who we are.
The Lay out:
We want about 4-5 Tabs that will help guide our customers through our website with ease. Some ideas of what we want to call the tabs might be….
1. Home
- This tab will take them to the home page
2. Contact Us
- Our contact information
- Client contact form
- Some sort of membership form?
3. Pick-up Service
- This tab will explain how this process works and what it in tells.
- This page will also have a section for requirements.
- This pickup service will only be available for members and people that have a good account with us.
4. How it Works
- This page will explain who we are and how we work.
- I would like to somehow creatively show the process and the steps we take in melting their gold.
Effects:
An effect that I would want to see is a live precious metal stock price. This price will automatically update and post the most recent and current price on the market of what the gold, silver etc prices. Here is a link of a company that has something similar, http://kelvaro-refining.example/ what I like about this spot price pop up, is that it follows them all over the page. I like that idea.
I would also like some sort of slide show that has videos and demonstrations of our company and business.
These are all Websites of our competitors that we like many ideas from.
http://www.hlpmr.example/
What we like about this website is the tab that says “Request Pick-up” With a form that they have to fill out. We would want more than just a form; we would want some sort of membership application.
http://dovemetals.example/
What I like about this website is the slideshow. It’s very simple yet professional. This is something that I would like to incorporate into our website. I also like the live metal market price.
http://kelvaro-refining.example/
This is another example of a website that has a live spot price of the gold market. I like how the gold price follows you around the page. I would like to see some of your ideas with this.
http://www.quillmetals.example/
This website is very clean and simple. I like the colors. I would like a little more character than what they have but I like the simplicity.
The colors we like are black, white, silver, gold, Royal Blue etc; basically anything that creates a clean atmosphere. These colors match our logo and also have a very elegant and professional perception to them. Please do not limit yourselves to only our suggestions
These are links to our Logo with all different colors.
https://www.filecrate.example/s/a11b22c33d44e55/LOGO_black_background.png
https://www.filecrate.example/s/f66g77h88i99j00/LOGO_black.png
https://www.filecrate.example/s/k12l34m56n78o90/LOGO_transparent_background.png
https://www.filecrate.example/s/p21q43r65s87t09/LOGO_white_background.png
These are links to a brochure of our business that represents and shows the process of what we do and demonstrates who we are.
https://www.filecrate.example/s/u13v35w57x79y91/inside_1.pdf
https://www.filecrate.example/s/z24a46b68c80d02/inside_2.pdf
Bottom line we want to see examples of ideas and layouts that you have for a website. Please upload them and We will comment back on them.

```html
<!DOCTYPE html>
<html lang="en">
<head>
<meta charset="utf-8">
<title>Harborline Refinery – Scrap Calculator</title>
<link href="https://fonts.googleapis.com/css2?family=Cinzel:wght@400;600&family=PT+Sans:ital,wght@0,400;0,700;1,400&display=swap" rel="stylesheet">
<style>
:root{
  --black:#000;
  --ink:#0b0b0b;
  --gold:#c9a24f;
  --gold-text:#b8913f;
  --gold-light:#d9bf86;
  --tan-top:#c9ad7a;
  --tan-bot:#9c7f4c;
  --grey-top:#6a6a6a;
  --grey-bot:#3a3a3a;
  --red-top:#d11616;
  --red-bot:#8c0202;
  --white:#fff;
  --footer:#151515;
}
*{box-sizing:border-box;margin:0;padding:0}
html,body{width:1200px;height:896px;overflow:hidden;background:var(--black)}
body{font-family:"PT Sans",sans-serif;color:var(--white);position:relative}
.abs{position:absolute}

.brand{left:204px;top:36px;font-family:"PT Sans",sans-serif;font-size:26px;font-weight:400;color:var(--gold-light);letter-spacing:2px}
.lang{left:726px;top:44px;width:86px;height:22px;border-radius:2px;background:linear-gradient(#fff,#dcdcdc);color:#333;font-size:11px;display:flex;align-items:center;padding-left:6px;gap:6px}
.lang .flag{width:16px;height:11px;background:linear-gradient(#2a3f8f,#b82a35)}
.lang svg{margin-left:auto;margin-right:6px}
.search{left:821px;top:44px;width:180px;height:22px;border-radius:2px;background:linear-gradient(#fff,#d9d9d9);color:#333;font-size:9px;display:flex;align-items:center;padding-left:14px}
.search svg{position:absolute;right:8px;top:5px}

.nav{left:0;top:99px;width:1200px;height:61px;background:linear-gradient(#707070,#4a4a4a);display:flex;padding-left:180px}
.nav-item{width:170px;height:61px;border-left:1px solid #2e2e2e;padding:16px 0 0 21px}
.nav-item:last-child{border-right:1px solid #2e2e2e}
.nav-item b{display:block;font-weight:400;font-size:14px;letter-spacing:-.2px}
.nav-item i{display:block;font-size:11px;color:#c8c8c8;margin-top:4px}
.nav-item.active{background:linear-gradient(#c9ac76,#917645)}
.nav-item.active b{color:#f3e6c8}
.nav-item.active i{color:#3e2f12}

.title{left:0;width:1200px;top:195px;text-align:center;font-family:"Cinzel",serif;font-size:24px;font-weight:400;color:var(--gold-light);letter-spacing:.5px}

.panel{left:268px;top:245px;width:639px;height:433px;border:1px solid #3a3a3a;background:var(--ink)}
.note{left:0;width:1200px;text-align:center;color:var(--gold-text);font-size:13.5px;line-height:20.5px}

.row{left:339px;height:30px;display:flex;gap:2px}
.cell{height:30px;font-size:12.5px;display:flex;align-items:center;padding-left:11px}
.cell.label{width:160px;background:linear-gradient(var(--grey-top),var(--grey-bot))}
.cell.input{width:161px;background:linear-gradient(#5c5c5c,#363636)}
.cell.value{width:162px;background:linear-gradient(var(--tan-top),var(--tan-bot))}

.btn{top:523px;height:40px;background:linear-gradient(var(--red-top),var(--red-bot));display:flex;align-items:center;justify-content:center;font-size:13.5px;gap:38px}
.btn.clear{left:501px;width:161px}
.btn.calc{left:664px;width:163px}
.total-label{left:600px;top:575px;font-size:12.5px;color:var(--gold-light)}

.footer{left:0;top:766px;width:1200px;height:53px;background:var(--footer)}
.footer .brand-small{left:203px;top:17px;font-family:"PT Sans",sans-serif;font-size:14px;font-weight:400;letter-spacing:1px;color:var(--gold-light)}
.footer .copy{left:354px;top:21px;font-size:9.5px;color:#bbb}
.socials{right:200px;top:20px;display:flex;gap:22px}
.socials span{width:12px;height:12px;border-radius:50%;background:#6f6f6f;display:block}

.ticker{left:0;top:819px;width:1200px;height:77px;background:linear-gradient(#c7ab78,#9f8453)}
.t-label{top:23px;font-size:9px;color:#2a2010}
.t-box{top:38px;height:19px;border-radius:2px;background:linear-gradient(#8d7345,#a68b59);box-shadow:inset 0 1px 2px rgba(0,0,0,.45);font-size:8px;color:#f2e6cc;display:flex;align-items:center;padding-left:7px}
.t-box.num{justify-content:center;padding-left:0}
.sep{top:14px;width:1px;height:50px;background:#8a6f42;box-shadow:1px 0 0 #d2ba8c}
</style>
</head>
<body>
<header>
  <div class="abs brand">HARBORLINE REFINERY</div>
  <div class="abs lang"><span class="flag" role="img" aria-label="United Kingdom flag"></span>English
    <svg width="7" height="5" viewBox="0 0 7 5"><path d="M0 0l3.5 4L7 0" fill="none" stroke="#333" stroke-width="1.4"/></svg></div>
  <div class="abs search">SEARCH
    <svg width="12" height="12" viewBox="0 0 12 12"><circle cx="5" cy="5" r="3.8" fill="none" stroke="#888" stroke-width="1.4"/><path d="M8 8l3 3" stroke="#888" stroke-width="1.6"/></svg></div>
</header>

<nav class="abs nav">
  <div class="nav-item"><b>HOME</b><i>Welcome to our Site</i></div>
  <div class="nav-item"><b>PICKUP SERVICE</b><i>Get our services Free</i></div>
  <div class="nav-item"><b>HOW IT WORKS</b><i>Did you know our works</i></div>
  <div class="nav-item active"><b>SCRAP CALCULATOR</b><i>Gold Scrap Caclulator</i></div>
  <div class="nav-item"><b>CONTACT US</b><i>Get in Touch</i></div>
</nav>

<main>
  <h1 class="abs title">STEP ONE - VERIFICATION</h1>
  <section class="abs panel"></section>
  <p class="abs note" style="top:267px">PLEASE ENTER YOUR GRAM WEIGHT BELOW AND WAIT<br>A FEW SECONDS FOR YOUR ESTIMATED QUOTE</p>

  <div class="abs row" style="top:323px"><div class="cell label">10K GOLD</div><div class="cell input"></div><div class="cell value">$0.00</div></div>
  <div class="abs row" style="top:356px"><div class="cell label">14K GOLD</div><div class="cell input"></div><div class="cell value">$0.00</div></div>
  <div class="abs row" style="top:390px"><div class="cell label">DENTAL GOLD</div><div class="cell input"></div><div class="cell value">$0.00</div></div>
  <div class="abs row" style="top:423px"><div class="cell label">18K GOLD</div><div class="cell input"></div><div class="cell value">$0.00</div></div>
  <div class="abs row" style="top:457px"><div class="cell label">22K GOLD</div><div class="cell input"></div><div class="cell value">$0.00</div></div>
  <div class="abs row" style="top:490px"><div class="cell label">.925 SILVER</div><div class="cell input"></div><div class="cell value">$0.00</div></div>

  <div class="abs btn clear"><span>CLEAR</span>
    <svg width="16" height="16" viewBox="0 0 16 16"><circle cx="8" cy="8" r="7.5" fill="#eee"/><path d="M5 5l6 6M11 5l-6 6" stroke="#b30a0a" stroke-width="2"/></svg></div>
  <div class="abs btn calc"><span>CALCULATER</span>
    <svg width="16" height="16" viewBox="0 0 16 16"><circle cx="8" cy="8" r="7.5" fill="#eee"/><path d="M4.5 8.2l2.4 2.4 4.6-5" fill="none" stroke="#555" stroke-width="2"/></svg></div>

  <div class="abs total-label">TOTAL :</div>
  <div class="abs row" style="top:566px;left:664px"><div class="cell value">$0.00</div></div>

  <p class="abs note" style="top:618px">PRICE QUOTES ARE UP TO THE MINUTE LIVE GOLD SPOT<br>PRICES ARE BASED ON 31.1 GRAMS TO A TROY OUNCE</p>
</main>

<footer class="abs footer">
  <div class="abs brand-small">HARBORLINE</div>
  <div class="abs copy">Copyrights ©2013. Harborline Refinery. All rights reserved.</div>
  <div class="abs socials"><span></span><span></span><span></span><span></span><span></span></div>
</footer>

<aside class="abs ticker">
  <div class="abs t-label" style="left:203px">REAL-TIME PRICE</div>
  <div class="abs t-box" style="left:201px;width:146px">GOLD
    <svg style="position:absolute;right:4px;top:4px" width="11" height="11" viewBox="0 0 11 11"><rect width="11" height="11" rx="1" fill="#e8dcc0"/><path d="M3 4l2.5 3L8 4" fill="#6d5430"/></svg></div>
  <div class="abs sep" style="left:363px"></div>
  <div class="abs t-label" style="left:378px">LAST UPDATE
    <svg style="vertical-align:-2px;margin-left:3px" width="11" height="11" viewBox="0 0 11 11"><rect width="11" height="11" rx="1" fill="#fff"/><rect width="11" height="3" fill="#d22"/></svg></div>
  <div class="abs t-box" style="left:377px;width:146px">THU MAY 30, 6:29 AM CDT</div>
  <div class="abs sep" style="left:537px"></div>
  <div class="abs t-label" style="left:553px">BID</div>
  <div class="abs t-box num" style="left:551px;width:60px">1,400.36</div>
  <div class="abs t-label" style="left:621px">ASK</div>
  <div class="abs t-box num" style="left:620px;width:60px">1,400.98</div>
  <div class="abs sep" style="left:694px"></div>
  <div class="abs t-label" style="left:710px">LOW</div>
  <div class="abs t-box num" style="left:709px;width:60px">1,389.12</div>
  <div class="abs t-label" style="left:779px">HIGH</div>
  <div class="abs t-box num" style="left:777px;width:60px">1,410.86</div>
  <div class="abs sep" style="left:852px"></div>
  <div class="abs t-label" style="left:868px">CHANGE</div>
  <div class="abs t-box num" style="left:867px;width:69px">+6.99 (0.5%)</div>
  <div class="abs sep" style="left:953px"></div>
  <svg class="abs" style="left:968px;top:22px" width="34" height="34" viewBox="0 0 34 34"><path d="M27 17a10 10 0 1 1-6-9.2" fill="none" stroke="#5a5a55" stroke-width="4"/><path d="M17 2l8 6-9 3z" fill="#5a5a55"/></svg>
</aside>
</body>
</html>
```